Business card design needed

We need something on the back that allows the customer to get five stamps then the sixth visit they get 25 dollars to spend.
Business
Quality meat,value for money,spit roast hire, wholesale pubs clubs,cater for bbqs.kessel lane butchery 58 kessel lane.64390217.

```html
<!DOCTYPE html>
<html lang="en">
<head>
<meta charset="utf-8">
<title>Kessel Lane Butchery – Loyalty Card</title>
<link rel="stylesheet" href="https://fonts.googleapis.com/css2?family=Crimson+Text:wght@700&display=swap">
<style>
  :root {
    --pink-light: #f8a9be;
    --pink-mid: #f59cb4;
    --pink-deep: #f08ea9;
    --plum: #690d40;
    --plum-border: #6b1446;
    --white: #ffffff;
    --lilac-text: #d2b2d2;
    --illustration-a: #b78fb6;
    --illustration-b: #8d6790;
  }
  html, body {
    margin: 0;
    padding: 0;
    overflow: hidden;
    background: #ffffff;
  }
  .loyalty-card {
    position: relative;
    width: 1200px;
    height: 741px;
    overflow: hidden;
    background: radial-gradient(ellipse at 50% 35%, var(--pink-light) 0%, var(--pink-mid) 55%, var(--pink-deep) 100%);
    font-family: "Crimson Text", Georgia, serif;
  }
  .offer-band {
    position: absolute;
    left: 0;
    top: 51px;
    width: 1200px;
    height: 195px;
    background: var(--plum);
  }
  .butcher-illustration {
    position: absolute;
    left: 50px;
    top: 36px;
    width: 186px;
    height: 231px;
  }
  .offer-text {
    position: absolute;
    left: 260px;
    top: 62px;
    width: 906px;
    margin: 0;
    text-align: center;
    color: var(--white);
    font-weight: 700;
    font-size: 44px;
    line-height: 56px;
    letter-spacing: 0.3px;
  }
  .stamp-row {
    position: absolute;
    left: 32px;
    top: 377px;
    display: flex;
    gap: 19px;
  }
  .stamp-box {
    box-sizing: border-box;
    width: 212px;
    height: 210px;
    background: var(--white);
    border: 2.5px solid var(--plum-border);
    border-radius: 44px;
    display: flex;
    align-items: center;
    justify-content: center;
    text-align: center;
    color: var(--lilac-text);
    font-weight: 700;
    font-size: 50px;
    line-height: 56px;
  }
</style>
</head>
<body>
  <main class="loyalty-card">
    <div class="offer-band"></div>

    <svg class="butcher-illustration" viewBox="0 0 186 231" role="img" aria-label="Illustration of a butcher in a red cap and apron sharpening a knife, with a side of meat behind him">
      <defs>
        <radialGradient id="illustrationTone" cx="50%" cy="45%" r="60%">
          <stop offset="0%" stop-color="var(--illustration-a)"/>
          <stop offset="100%" stop-color="var(--illustration-b)"/>
        </radialGradient>
      </defs>
      <ellipse cx="93" cy="115.5" rx="91" ry="113" fill="url(#illustrationTone)" stroke="var(--plum)" stroke-width="4"/>
    </svg>

    <p class="offer-text">
      spend $50 or more to recieve a stamp<br>
      &amp;<br>
      recieve $25 off your 6th visit
    </p>

    <section class="stamp-row" aria-label="Stamp boxes">
      <div class="stamp-box">Visit<br>1</div>
      <div class="stamp-box">Visit<br>2</div>
      <div class="stamp-box">Visit<br>3</div>
      <div class="stamp-box">Visit<br>4</div>
      <div class="stamp-box">Visit<br>5</div>
    </section>
  </main>
</body>
</html>
```